Electrical Contracting Business Website

Require website done for my contracting business.
Partly done one but really dont have time.

You can view the current one at http://brelton.net.au

You can use any info/styles/photos from the current website

I like the orange color of the logo so id like things to be with that
Unfortunatly being a new business (Sept 2015) I havent got alot of photos . but if you require any for any of the specifics listed in the doc file ill have a look to see what I have.

I am targeting mainly commercial / industrial clients. Which also includes government and mining.

Target Market(s)

People requiring electricians

Industry/Entity Type

Electrician

Coding

Number of Pages Required

Colors
f37122

Requirements
Must have
• logo with EC Number
• Keep it simple and not to complicated
• Comply with the current html / style sheet standards.
• Desktop/Mobile Version compatability
Nice to have
• additional photos.
• The domestic lifts we install are by vostrel I dont have any photos of them unfortunately.
Should not have
• change colour of logo

```html
<!DOCTYPE html>
<html lang="en">
<head>
<meta charset="utf-8">
<title>Brelton Engineering</title>
<link href="https://fonts.googleapis.com/css2?family=Oswald:wght@400;500&family=Open+Sans:wght@400;600;700&display=swap" rel="stylesheet">
<style>
:root{
  --orange:#f37122;
  --dark:#3a3a3a;
  --darker:#2a2a2a;
  --footer:#333;
  --text:#777;
  --line:#e2e2e2;
  --white:#fff;
}
*{box-sizing:border-box;margin:0;padding:0}
html,body{width:1200px;height:3098px;overflow:hidden}
body{font-family:"Open Sans",Arial,sans-serif;color:var(--text);background:var(--white);position:relative}
.abs{position:absolute}
h2.section-title{font-family:"Oswald","Arial Narrow",sans-serif;font-weight:400;font-size:29px;color:#333;text-align:center;text-transform:uppercase}
.rule{width:34px;height:3px;background:var(--orange);margin:20px auto 0}
.lead{font-size:12.5px;line-height:20px;text-align:center;color:#888}
.notch{position:absolute;left:50%;margin-left:-12px;width:0;height:0;border-left:12px solid transparent;border-right:12px solid transparent;border-top:12px solid var(--c)}

/* header */
.topbar{left:0;top:0;width:1200px;height:28px}
.header{left:0;top:0;width:1200px;height:98px}
.logo{left:222px;top:24px;display:flex;align-items:center;gap:8px}
.logo-mark{width:34px;height:34px;border-radius:50%;background:var(--orange)}
.logo-name{font-family:"Open Sans",sans-serif;font-weight:700;font-size:30px;color:var(--orange);letter-spacing:1px}
.ec-no{left:266px;top:66px;font-size:9px;color:#888}
.badge{left:522px;top:40px;width:96px;height:42px;background:#e8ecf2;border-radius:3px}
.contact-top{left:723px;top:44px;font-size:12px;line-height:19px;color:#444}
.contact-top .mail{color:var(--orange)}
.btn-quote{left:913px;top:47px;width:105px;height:34px;background:var(--orange);color:#fff;font-family:"Oswald",sans-serif;font-size:13px;line-height:34px;text-align:center;text-transform:uppercase}
.nav{left:0;top:98px;width:1200px;height:40px;background:var(--dark)}
.nav ul{position:absolute;right:176px;top:0;display:flex;gap:0;list-style:none}
.nav li{font-size:11px;font-weight:700;color:#fff;text-transform:uppercase;line-height:40px;padding:0 11px}
.nav li.active{background:#2b2b2b}

/* hero */
.hero{left:0;top:138px;width:1200px;height:384px;background:linear-gradient(100deg,#d9d7d2 0%,#b8b6ad 30%,#6a7a88 55%,#32425a 75%,#a7a8ab 100%)}
.hero-caption{left:719px;top:252px;width:307px;height:161px;background:rgba(40,40,40,.88)}
.hero-caption h3{font-family:"Oswald",sans-serif;font-weight:500;font-size:18px;color:#fff;text-transform:uppercase;letter-spacing:.5px;background:#1c1c1c;padding:10px 18px;line-height:28px}
.hero-caption p{font-size:11px;line-height:17px;color:#ddd;padding:10px 22px 0}
.hero-caption .btn{margin:12px 0 0 22px;display:inline-block;background:var(--orange);color:#fff;font-size:9.5px;font-weight:600;padding:6px 12px;text-transform:uppercase}
.dots{left:540px;top:497px;display:flex;gap:8px}
.dots span{width:36px;height:5px;background:#fff}
.dots span.on{background:var(--orange)}

/* about */
.about-title{left:0;top:580px;width:1200px}
.about-text{left:230px;top:660px;width:740px}
.sector-band{left:0;top:836px;width:1200px;height:240px;background:var(--dark)}
.sector{width:270px;top:775px}
.sector .photo{width:270px;height:160px}
.sector h4{font-family:"Oswald",sans-serif;font-weight:400;font-size:20px;color:#fff;text-align:center;margin-top:25px;text-transform:uppercase}
.sector p{font-size:10.5px;line-height:16px;color:#888;text-align:center;margin-top:8px;padding:0 14px}

/* services */
.services-title{left:0;top:1136px;width:1200px}
.services-text{left:230px;top:1214px;width:740px}
.grid{left:172px;top:1310px;width:828px;display:grid;grid-template-columns:repeat(6,138px)}
.cell{height:138px;border-right:1px solid var(--line);text-align:center;padding-top:18px}
.cell:nth-child(6n){border-right:none}
.cell:nth-child(-n+6){border-bottom:1px solid var(--line)}
.cell svg{width:30px;height:30px}
.cell .name{font-size:11px;color:#666;margin-top:8px;display:block}
.cell .details{display:inline-block;margin-top:8px;border:1px solid #999;border-radius:3px;font-size:10px;color:#666;padding:1px 7px}

/* projects */
.projects{left:0;top:1656px;width:1200px;height:522px;background:radial-gradient(circle at 40% 45%,#4a4a4a 0%,#2c2c2c 55%,#1c1c1c 100%)}
.projects-title{left:0;top:1714px;width:1200px}
.projects-title h2{color:#fff}
.projects-text{left:230px;top:1792px;width:740px}
.projects-text .lead{color:#bbb}
.project-card{left:178px;top:1892px;width:848px;height:235px;background:rgba(15,15,15,.85)}
.project-photo{left:0;top:0;width:260px;height:235px;border:5px solid #fff;background:linear-gradient(135deg,#c9c2ae,#6b2a1e 45%,#d4c86a 80%,#3a3a3a)}
.project-info{left:298px;top:30px;width:520px}
.project-info h3{font-family:"Oswald",sans-serif;font-weight:400;font-size:22px;color:var(--orange)}
.project-info .sub{font-size:12.5px;color:#eee;margin-top:4px}
.project-info .meta{font-size:11px;color:#999;margin-top:18px;line-height:24px}
.project-info .btn{display:inline-block;margin-top:22px;background:var(--orange);color:#fff;font-size:10px;font-weight:700;padding:8px 13px;text-transform:uppercase}

/* clients */
.clients{left:0;top:2178px;width:1200px;height:192px}
.clients .arrow{position:absolute;top:80px}
.client{position:absolute;top:76px;width:150px;display:flex;align-items:center;justify-content:center;gap:8px;font-size:16px;font-weight:600;color:#999}
.client i{width:16px;height:16px;background:#bbb;display:block}

/* cta */
.cta{left:0;top:2370px;width:1200px;height:228px;background:var(--orange);text-align:center;color:#fff}
.cta h3{font-size:19px;font-weight:600;margin-top:47px}
.cta .phone{font-size:26px;font-weight:700;margin-top:18px;display:flex;justify-content:center;align-items:center;gap:10px}
.cta ul{list-style:none;display:flex;justify-content:center;margin-top:20px}
.cta li{font-size:10.5px;font-weight:700;text-transform:uppercase;padding:0 12px}

/* map */
.map{left:0;top:2598px;width:1200px;height:417px;background:linear-gradient(120deg,#e9e6df 0%,#dfe6d8 35%,#ece8e0 60%,#d9e3d0 100%)}
.find-card{left:465px;top:2664px;width:268px;height:252px;background:#fff;box-shadow:0 1px 6px rgba(0,0,0,.2);text-align:center}
.find-card h4{font-size:18px;font-weight:400;color:#333;padding:18px 0 14px;border-bottom:1px solid var(--line)}
.find-card .addr{font-size:11.5px;line-height:19px;color:#555;margin-top:14px}
.find-card .tel{font-size:11.5px;line-height:22px;color:#555;margin-top:12px}
.find-card .tel b{color:var(--orange);font-weight:400;margin-right:8px}
.find-card .mail{font-size:15px;color:var(--orange);margin-top:6px}
.pin{left:802px;top:2765px}

/* footer */
.footer{left:0;top:3015px;width:1200px;height:83px;background:var(--footer)}
.copy{left:173px;top:34px;font-size:10px;color:#bbb}
.social{left:528px;top:23px;display:flex;gap:10px}
.social span{width:29px;height:29px;border:1.5px solid var(--orange);border-radius:50%}
.to-top{left:576px;top:-14px;width:48px;height:14px}
</style>
</head>
<body>

<!-- header -->
<svg class="abs topbar" width="1200" height="28" viewBox="0 0 1200 28"><path d="M408 0H1200V28H430Z" fill="#3a3a3a"/>
  <circle cx="942" cy="14" r="4" fill="#fff"/><circle cx="965" cy="14" r="4" fill="#fff"/><circle cx="988" cy="14" r="4" fill="#fff"/><circle cx="1011" cy="14" r="4" fill="#fff"/></svg>
<div class="abs logo"><span class="logo-mark"></span><span class="logo-name">BRELTON</span></div>
<div class="abs ec-no">EC 40917 · Electrical Contractor</div>
<div class="abs badge" aria-label="Industry membership badge"></div>
<div class="abs contact-top"><div class="mail">info@brelton.net.au</div><div>+61 0400 112 358</div></div>
<div class="abs btn-quote">Get a Quote</div>
<nav class="abs nav"><ul>
  <li class="active">Home</li><li>About Us</li><li>Residential</li><li>Commercial</li><li>Industrial</li><li>Recent Projects</li><li>Contact Us</li>
</ul></nav>

<!-- hero -->
<div class="abs hero" role="img" aria-label="Electrician in hard hat testing a switchboard with a multimeter"></div>
<div class="abs hero-caption">
  <h3>Residential Electrical Work</h3>
  <p>Lorem ipsum dolor sit amet, consectetuer adipis cing elit, sed diam nonummy nibh</p>
  <span class="btn">Get a Quote</span>
</div>
<div class="abs dots"><span></span><span class="on"></span><span></span></div>
<div class="notch" style="--c:#fff;top:522px"></div>

<!-- about -->
<div class="abs about-title"><h2 class="section-title">About Us</h2><div class="rule"></div></div>
<div class="abs about-text"><p class="lead">Vel illum dolore eu feugiat nulla facilisis at vero eros et accumsan et iusto odio dignissim qui blandit praesent luptatum zzril delenit augue duis dolore te feugait nulla facilisi. Nam liber tempor cum soluta nobis eleifend option congue nihil imperdiet doming id quod mazim placerat facer possim assum. Typi non habent claritatem insitam</p></div>
<div class="abs sector-band"></div>
<div class="abs sector" style="left:173px"><div class="photo" role="img" aria-label="Residential switchboard" style="background:linear-gradient(135deg,#dcdcd6,#9ea29c)"></div><h4>Residential</h4><p>Lorem ipsum dolor sit amet, consectetuer adipiscing elit, sed diam nonummy nibh eu smod tincidunt ut laoreet dolore magna</p></div>
<div class="abs sector" style="left:465px"><div class="photo" role="img" aria-label="Commercial distribution board" style="background:linear-gradient(135deg,#5b5c5e,#b9b8b2 50%,#3e3f42)"></div><h4>Commercial</h4><p>Lorem ipsum dolor sit amet, consectetuer adipiscing elit, sed diam nonummy nibh eu smod tincidunt ut laoreet dolore magna</p></div>
<div class="abs sector" style="left:758px"><div class="photo" role="img" aria-label="Industrial circuit breakers" style="background:linear-gradient(135deg,#cfd0cd,#8c8f8f 55%,#3b3c3e)"></div><h4>Industrial</h4><p>Lorem ipsum dolor sit amet, consectetuer adipiscing elit, sed diam nonummy nibh eu smod tincidunt ut laoreet dolore magna</p></div>
<div class="notch" style="--c:#3a3a3a;top:1076px"></div>

<!-- services -->
<div class="abs services-title"><h2 class="section-title">Our General Services</h2><div class="rule"></div></div>
<div class="abs services-text"><p class="lead">Duis dolore te feugait nulla facilisi. Nam liber tempor cum soluta nobis eleifend option congue nihil imperdiet doming id quod mazim placerat facer possim assum. Typi non habent claritatem insitam</p></div>
<div class="abs grid">
  <div class="cell"><svg viewBox="0 0 30 30"><path d="M5 25L19 11M11 5l14 14M17 5l8 8-3 3-8-8z" stroke="#f37122" stroke-width="3" fill="none"/></svg><span class="name">Electrical Installations</span><span class="details">Details</span></div>
  <div class="cell"><svg viewBox="0 0 30 30"><rect x="7" y="4" width="10" height="16" rx="2" transform="rotate(-35 12 12)" fill="#f37122"/><path d="M17 18l8 8" stroke="#f37122" stroke-width="3"/></svg><span class="name">Voice and Data Cabling</span><span class="details">Details</span></div>
  <div class="cell"><svg viewBox="0 0 30 30"><circle cx="20" cy="10" r="7" fill="#f37122"/><circle cx="20" cy="10" r="3" fill="#fff"/><path d="M15 15L5 25" stroke="#f37122" stroke-width="4"/></svg><span class="name">Electrical Modifications</span><span class="details">Details</span></div>
  <div class="cell"><svg viewBox="0 0 30 30"><circle cx="12" cy="12" r="8" stroke="#f37122" stroke-width="3" fill="none"/><path d="M18 18l8 8" stroke="#f37122" stroke-width="4"/></svg><span class="name">Fault Finding</span><span class="details">Details</span></div>
  <div class="cell"><svg viewBox="0 0 30 30"><path d="M15 3l9 10h-6v14h-6V13H6z" fill="#f37122"/></svg><span class="name">Panel Upgrades</span><span class="details">Details</span></div>
  <div class="cell"><svg viewBox="0 0 30 30"><path d="M4 9l8-3v18l-8-3z M14 6h12v18H14z" fill="#f37122"/></svg><span class="name">Security Lighting</span><span class="details">Details</span></div>
  <div class="cell"><svg viewBox="0 0 30 30"><rect x="4" y="5" width="22" height="20" rx="2" fill="#f37122"/><path d="M16 9l-5 7h4l-1 5 5-7h-4z" fill="#fff"/></svg><span class="name">Generator Hookup</span><span class="details">Details</span></div>
  <div class="cell"><svg viewBox="0 0 30 30"><circle cx="15" cy="15" r="12" fill="#f37122"/><path d="M17 6l-7 10h5l-2 8 7-10h-5z" fill="#fff"/></svg><span class="name">Surge Protection</span><span class="details">Details</span></div>
  <div class="cell"><svg viewBox="0 0 30 30"><path d="M15 4L3 15h4v11h16V15h4z" fill="#f37122"/><rect x="12" y="18" width="6" height="8" fill="#fff"/></svg><span class="name">Building Maintenance</span><span class="details">Details</span></div>
  <div class="cell"><svg viewBox="0 0 30 30"><rect x="8" y="3" width="14" height="24" fill="#f37122"/><path d="M15 7l-3 4h6zM15 23l-3-4h6z" fill="#fff"/></svg><span class="name">Lift Maintenance</span><span class="details">Details</span></div>
  <div class="cell"><svg viewBox="0 0 30 30"><path d="M15 3v10c0 5 6 5 6 10s-8 5-9 1" stroke="#f37122" stroke-width="3.5" fill="none"/></svg><span class="name">Crane/Hoist Maintenance</span><span class="details">Details</span></div>
  <div class="cell"><svg viewBox="0 0 30 30"><path d="M4 21a11 11 0 0 1 22 0z" fill="#f37122"/><rect x="2" y="21" width="26" height="4" fill="#f37122"/></svg><span class="name">Labour Hire</span><span class="details">Details</span></div>
</div>
<div class="notch" style="--c:#fff;top:1656px;z-index:2"></div>

<!-- projects -->
<div class="abs projects" role="img" aria-label="Dim close-up of heavy electric motor machinery"></div>
<div class="abs projects-title"><h2 class="section-title">Our Recent Projects</h2><div class="rule"></div></div>
<div class="abs projects-text"><p class="lead">Duis dolore te feugait nulla facilisi. Nam liber tempor cum soluta nobis eleifend option congue nihil imperdiet doming id quod mazim placerat facer possim assum. Typi non habent claritatem insitam</p></div>
<div class="abs project-card">
  <div class="abs project-photo" role="img" aria-label="Hoist control panel with red emergency stop buttons"></div>
  <div class="abs project-info">
    <h3>TORVA Liftdeck 5000</h3>
    <p class="sub">Commissioning and maintenance of a 5 tonne Materials Hoist.</p>
    <p class="meta">Client: Liftline Torque Co<br>Location: Stonegate Builders - Harbour Square - Central City</p>
    <span class="btn">Know More</span>
  </div>
</div>
<div class="notch" style="--c:#1c1c1c;top:2178px"></div>

<!-- clients -->
<div class="abs clients">
  <svg class="arrow" style="left:150px" width="12" height="20" viewBox="0 0 12 20"><path d="M10 2L2 10l8 8" stroke="#777" stroke-width="2" fill="none"/></svg>
  <svg class="arrow" style="left:1036px" width="12" height="20" viewBox="0 0 12 20"><path d="M2 2l8 8-8 8" stroke="#777" stroke-width="2" fill="none"/></svg>
  <div class="client" style="left:190px"><i></i>KR Construction</div>
  <div class="client" style="left:350px"><i></i>Durnell</div>
  <div class="client" style="left:520px"><i></i>Novira Systems</div>
  <div class="client" style="left:690px"><i></i>Corbel Group</div>
  <div class="client" style="left:850px"><i></i>Bram Foods</div>
</div>

<!-- contact call to action -->
<div class="abs cta">
  <h3>Contact Us Today - We Answer Our Phone 24/7</h3>
  <div class="phone"><svg width="24" height="24" viewBox="0 0 24 24"><path d="M6 2l4 5-2 3c1 3 3 5 6 6l3-2 5 4-3 4C10 22 2 14 2 5z" fill="#fff"/></svg>+61 0400 112 358</div>
  <ul><li>Home</li><li>About Us</li><li>Residential</li><li>Commercial</li><li>Industrial</li><li>Recent Projects</li><li>Contact Us</li></ul>
</div>
<div class="notch" style="--c:#f37122;top:2598px;z-index:2"></div>

<!-- map -->
<div class="abs map" role="img" aria-label="Street map of the business location"></div>
<svg class="abs pin" width="28" height="40" viewBox="0 0 28 40"><path d="M14 0a14 14 0 0 1 14 14c0 10-14 26-14 26S0 24 0 14A14 14 0 0 1 14 0z" fill="#f37122"/><circle cx="14" cy="14" r="5" fill="#fff"/></svg>
<div class="abs find-card">
  <h4>How to find us?</h4>
  <div class="addr">Brelton Engineering Pty Ltd<br>EC 40917<br>Kelmore Park, Western Australia, 6100.</div>
  <div class="tel"><b>&#9990;</b>+61 0400 112 358<br><b>&#9632;</b>+61 (08) 6100 2200</div>
  <div class="mail">info@brelton.net.au</div>
</div>

<!-- footer -->
<footer class="abs footer">
  <svg class="abs to-top" viewBox="0 0 48 14"><path d="M0 14L24 0l24 14z" fill="#333"/><path d="M18 11l6-5 6 5" stroke="#fff" stroke-width="1.5" fill="none"/></svg>
  <div class="abs copy">Copyright © Brelton 2016</div>
  <div class="abs social"><span></span><span></span><span></span><span></span></div>
</footer>

</body>
</html>
```